Gallerine Vault, LLC needs clean, modern business card design

Gallerine Vault is based in Honolulu. We offer fine arts collections management and documentation services for private and corporate art collectors. I would like to use my logo (attached). Card can be either single or double sided and either vertical or horizontal. My clients are businesses with art collections (banks, law firms, etc.) and wealthy individual collectors.

Industry/Entity Type

Business

```html
<!DOCTYPE html>
<html lang="en">
<head>
<meta charset="utf-8">
<title>Gallerine Vault, LLC — Business Card</title>
<link rel="stylesheet" href="https://fonts.googleapis.com/css2?family=Questrial&display=swap">
<style>
  :root {
    --page: #e6e3de;
    --card: #ffffff;
    --ink: #111111;
    --band: #1c1c1c;
    --band-text: #d8d8d8;
    --name-text: #ffffff;
    --brand: #2a2a2a;
    --sketch-light: #f4f4f4;
    --sketch-dark: #d9d9d9;
  }
  html, body {
    margin: 0;
    width: 1200px;
    height: 1200px;
    overflow: hidden;
    background: var(--page);
    font-family: "Questrial", "Helvetica Neue", Arial, sans-serif;
  }
  .canvas {
    position: relative;
    width: 1200px;
    height: 1200px;
  }
  .card {
    position: absolute;
    left: 100px;
    top: 314px;
    width: 1000px;
    height: 572px;
    background: var(--card);
    border-radius: 14px;
    box-shadow: 0 14px 40px rgba(0,0,0,0.18);
    overflow: hidden;
    color: var(--ink);
  }
  .brand {
    position: absolute;
    left: 64px;
    top: 40px;
    font-size: 52px;
    color: var(--brand);
    letter-spacing: 0.5px;
    line-height: 1;
    white-space: nowrap;
  }
  .tagline-band {
    position: absolute;
    left: 330px;
    right: 0;
    top: 108px;
    height: 30px;
    background: var(--band);
    color: var(--band-text);
    font-size: 20px;
    letter-spacing: 1.2px;
    line-height: 30px;
    text-align: right;
    padding-right: 40px;
    box-sizing: border-box;
    white-space: nowrap;
  }
  .name-plate {
    position: absolute;
    left: 0;
    top: 190px;
    width: 450px;
    height: 130px;
    background: var(--band);
    border-radius: 0 12px 12px 0;
    color: var(--name-text);
    box-sizing: border-box;
    padding: 14px 28px 0 40px;
    text-align: right;
  }
  .name-plate .name {
    font-size: 44px;
    letter-spacing: 2px;
    line-height: 1.15;
    white-space: nowrap;
  }
  .name-plate .role {
    font-size: 28px;
    letter-spacing: 1.5px;
    line-height: 1.2;
  }
  .contact {
    position: absolute;
    left: 40px;
    top: 384px;
    font-size: 22px;
    line-height: 26px;
    letter-spacing: 0.6px;
    white-space: nowrap;
  }
  .address-bar {
    position: absolute;
    left: 0;
    top: 450px;
    width: 660px;
    height: 38px;
    background: var(--band);
    color: var(--band-text);
    border-radius: 0 10px 10px 0;
    font-size: 20px;
    line-height: 38px;
    letter-spacing: 1px;
    padding-left: 40px;
    box-sizing: border-box;
    white-space: nowrap;
  }
  .portrait-sketch {
    position: absolute;
    right: 110px;
    top: 200px;
    width: 230px;
    height: 372px;
  }
</style>
</head>
<body>
  <main class="canvas">
    <section class="card" aria-label="Business card for Gallerine Vault, LLC">
      <div class="brand">Gallerine Vault</div>
      <div class="tagline-band">"Fine Arts Collections Management Services"</div>

      <div class="name-plate">
        <div class="name">Leilani M. Ostrow</div>
        <div class="role">Manager</div>
      </div>

      <div class="contact">
        <div class="email">hello@gallerinevault.com</div>
        <div class="web">www.gallerinevault.com</div>
      </div>

      <div class="address-bar">1420 Kapena Lane Honolulu, HI 96817 (808) 555-0148</div>

      <svg class="portrait-sketch" role="img" aria-label="Pale pencil-sketch illustration of a standing collector in a cap and jacket" viewBox="0 0 230 372" preserveAspectRatio="none">
        <defs>
          <linearGradient id="sketchTone" x1="0" y1="0" x2="0" y2="1">
            <stop offset="0" stop-color="#f4f4f4"/>
            <stop offset="1" stop-color="#d9d9d9"/>
          </linearGradient>
        </defs>
        <rect x="0" y="0" width="230" height="372" rx="10" fill="url(#sketchTone)"/>
      </svg>
    </section>
  </main>
</body>
</html>
```